Wine Label for a White and a Red Wine from Italy

We have a very good idea of what we want with artwork. We need you to please design a 'template' with the text so we can change out the artwork from year to year. Samples are shown of what we are looking for. We are looking for options with the two basic designs. Brand name of wine is: Valora del Torrino. Both wines are in a light green Bordeaux-style bottle (note: we don't show a light green bottle in the mockup but please remember the bottle is light green). Artwork is provided. We'd like to see either the green or blue butterfly on the white wine, the red butterfly is for the red wine. Please base the design on the attached label from Ashby and/or the attached label from Chateau Vellanges.

Target Market(s)

Millennials, women

Requirements
Must have
• The artwork (butterflies) attached.
Nice to have
• Elegant, readable fonts. Please make the text so it can be changed by the printer. Please make it so the artwork can be changed too.

```html
<!DOCTYPE html>
<html lang="en">
<head>
<meta charset="utf-8">
<title>Valora del Torrino – Rosso Label</title>
<link href="https://fonts.googleapis.com/css2?family=Marcellus+SC&family=Marcellus&display=swap" rel="stylesheet">
<style>
  :root {
    --backdrop-top: #dedcd0;
    --backdrop-bottom: #f3f2ee;
    --label-paper: #f7f7f6;
    --frame-red: #b23b36;
    --vintage-red: #b5362f;
    --ink: #474747;
    --ink-soft: #6d6d6d;
    --art-light: #f6dc8a;
    --art-main: #f0bd2e;
  }
  * { margin: 0; padding: 0; box-sizing: border-box; }
  html, body {
    width: 887px;
    height: 1200px;
    overflow: hidden;
  }
  body {
    background: linear-gradient(180deg, var(--backdrop-top), var(--backdrop-bottom));
    position: relative;
  }
  .label {
    position: absolute;
    left: 44px;
    top: 96px;
    width: 800px;
    height: 1008px;
    background: var(--label-paper);
    box-shadow: 0 2px 10px rgba(0,0,0,0.08);
  }
  .art-frame {
    position: absolute;
    left: 171px;
    top: 0;
    width: 466px;
    height: 448px;
    border: 6px solid var(--frame-red);
    border-top: none;
  }
  .artwork {
    width: 100%;
    height: 100%;
    display: block;
    background: linear-gradient(160deg, var(--art-light), var(--art-main));
  }
  .label-line {
    position: absolute;
    left: 0;
    width: 100%;
    text-align: center;
    line-height: 1;
    white-space: nowrap;
    color: var(--ink);
    font-family: "Marcellus SC", serif;
    font-weight: 400;
  }
  .brand-name { top: 540px; font-size: 54px; letter-spacing: 1px; }
  .cuvee { top: 640px; font-size: 30px; }
  .vintage { top: 692px; font-size: 48px; color: var(--vintage-red); font-family: "Marcellus", serif; }
  .wine-type { top: 758px; font-size: 31px; }
  .region { top: 804px; font-size: 31px; }
  .producer { top: 890px; font-size: 24px; }
  .producer .credit { color: var(--ink-soft); }
  .producer .by { font-family: "Marcellus", serif; }
  .farming { top: 938px; font-size: 21px; font-family: "Marcellus", serif; }
</style>
</head>
<body>
  <section class="label">
    <div class="art-frame">
      <div class="artwork" role="img" aria-label="Yearly label artwork: red butterfly over loose yellow brushstrokes"></div>
    </div>

    <h1 class="label-line brand-name">Valora Del Torrino</h1>
    <p class="label-line cuvee">Barrel Select</p>
    <p class="label-line vintage">2018</p>
    <p class="label-line wine-type">Rosso</p>
    <p class="label-line region">Piemonte, Italy</p>
    <p class="label-line producer"><span class="credit">ARTISANLY CRAFTED</span> <span class="by">by</span> CANTINA SETTE VALLI</p>
    <p class="label-line farming">sustainably farmed</p>
  </section>
</body>
</html>
```